Header Graphic for the Hazardous Materials field Manual Website

I need a graphic design for a website header for a new project I'm working on. The color scheme (which is not set in stone) can be seen at the following web address: http://vorplinetguide.com/
The header needs to have 3 versions. One for desktop, one for tablet and one for phone. The dimensions of the header are 980x108, 800x80, and 500x60, respectively.
The header graphic has to be designed to allow responsive resizing of the web pages, that is, as the browser window is resized, the left side of the graphic will disappear until a new breakpoint is reached. This means that the logo graphic has to be on the right hand side of the graphic header.
You can read through the Preface and Intro to get a feel for what the site is about but generally, it will be an electronic version of a technical document that allows site visitors to find help on different meters and analyzers used in the hazardous materials field.
I'm attaching the lomi circle logo (the best version I have) and will post the trust fund logo as soon as I can get the original artwork.
I would like the header graphic to somehow convey the instruments, sort of like the splash image used on the main page of the website.
Field inspectors
Graphic Design

```html
<!DOCTYPE html>
<html lang="en">
<head>
<meta charset="utf-8">
<title>Hazardous Material Field Manual — Header</title>
<link rel="stylesheet" href="https://fonts.googleapis.com/css2?family=Oswald:wght@400&display=swap">
<style>
  :root {
    --hazard-red: #e5191f;
    --deep-red: #b01217;
    --mid-grey: #c4c4c4;
    --night: #000000;
    --signal-green: #35e317;
    --glow-green: rgba(60, 255, 30, 0.55);
    --mask-grey: #3a3a3a;
    --mask-shadow: #121212;
    --symbol-red: #8a0c10;
  }
  * { margin: 0; padding: 0; box-sizing: border-box; }
  html, body {
    width: 1200px;
    height: 132px;
    overflow: hidden;
    background: var(--night);
  }
  .site-header {
    position: relative;
    width: 1200px;
    height: 132px;
    overflow: hidden;
    background: linear-gradient(90deg,
      var(--hazard-red) 0%,
      var(--hazard-red) 22%,
      var(--deep-red) 28%,
      var(--mid-grey) 40%,
      #5a5a5a 50%,
      var(--night) 58%,
      var(--night) 100%);
  }
  .hazard-symbol {
    position: absolute;
    left: 14px;
    top: 8px;
    width: 140px;
    height: 118px;
    border-radius: 50%;
    background: radial-gradient(circle, var(--symbol-red) 0%, rgba(138,12,16,0.6) 55%, rgba(138,12,16,0) 72%);
  }
  .mask-photo {
    position: absolute;
    left: 998px;
    top: 0;
    width: 150px;
    height: 132px;
    background: radial-gradient(ellipse at 50% 55%, var(--mask-grey) 0%, #262626 45%, var(--mask-shadow) 75%, rgba(0,0,0,0) 100%);
  }
  .site-title {
    position: absolute;
    left: 0;
    top: 0;
    width: 1200px;
    height: 132px;
  }
  .site-title text {
    font-family: "Oswald", "Arial Narrow", sans-serif;
    font-weight: 400;
    font-size: 76px;
    fill: var(--signal-green);
    filter: drop-shadow(0 0 3px var(--glow-green)) drop-shadow(0 0 6px var(--glow-green));
  }
</style>
</head>
<body>
  <header class="site-header">
    <div class="hazard-symbol" role="img" aria-label="Dark red biohazard warning symbol"></div>
    <div class="mask-photo" role="img" aria-label="Photograph of a gas mask on a dark background"></div>
    <svg class="site-title" viewBox="0 0 1200 132" aria-labelledby="title-text">
      <text id="title-text" x="141" y="96" textLength="857" lengthAdjust="spacingAndGlyphs">HAZARDOUS MATERIAL FIELD MANUAL</text>
    </svg>
  </header>
</body>
</html>
```